Marketing Services Overview PDF Booklet/Catalog

We need a professionally designed pdf booklet/catalog that gives an overview of our marketing agency services. We run ads and generate leads for concrete coating and epoxy flooring companies. This pdf design should be 10-12 pages show casing our marketing services/packages.
Here is a video I made going over the project design:
https://clips.vormelink.com/watch/Qm7TzKp2WxRb9cNv4HdLsE
-----------------------
Design Brief - Solutions Overview Doc
Notes: Would like this design to also be converted to a flexlo template for future adjustments.
Design brief video link: https://clips.vormelink.com/watch/Qm7TzKp2WxRb9cNv4HdLsE
Our Company Info:
FloorBright Digital
https://floorbrightdigital.com/
Sales slides: Overview - FloorBright System
Primary Colors:
Black
Blue
White
Secondary Colors:
Grey
Charcoal
Lite Blue
Red
Fonts:
Montserrat
Bebas Neue
Anton
Oxygen
Competitor websites:
https://surfaceignite.com/
https://tradevantor.com/
https://slabpromotionsquad.com/
https://www.builderpulse.click/
https://www.primerlayerads.com/
https://www.pipefixrank.net/
https://yardvista.marketing/
Target Client Websites:
https://glimmurfloors.com/
https://bayvaultshop.ca/
https://www.prairiestrongslabfinishes.com/
Design Brief for FloorBright Digital’s Services Booklet
Project Overview: FloorBright Digital is creating a multi-page PDF booklet that serves as a digital catalog outlining our comprehensive marketing services. This booklet will highlight our lead generation system and full marketing system, using a combination of text and illustrative visuals to communicate our processes and results effectively.
Target Audience:
Potential clients in the concrete coating and epoxy flooring industry.
Business owners seeking effective and scalable marketing solutions.
Objectives:
Showcase the effectiveness of our lead generation system.
Illustrate the benefits of our full marketing system.
Highlight the ease and effectiveness of using our services through visuals and real-life examples.
Design Requirements:
Style: Clean, professional, masculine, and modern. Use brand colors and fonts for consistency.
Layout: Balanced mix of text and visuals to maintain reader engagement. Ensure no page is overly cluttered.
Images: High-quality, relevant images of epoxy flooring, marketing visuals (ads, CRM, reviews), and diagrams.
Typography: Clear, readable fonts for headings and body text.
Icons/Graphics: Use icons for sections like CRM, text sequences, etc.
File Specifications:
Format: PDF, optimized for both digital viewing and print.
Dimensions: Standard 8.5" x 11" (letter size) or A4.
Additional Notes:
Ensure brand consistency across all pages.
Focus on user-friendly design that guides the reader naturally through the content.
Target Market(s)
concrete coating companies, epoxy flooring companies
Industry/Entity Type
digital marketing agency targeting home service/concrete coating companies
Font styles to use
Other font styles liked:
- Montserrat, Bebas Neue, Anton, Oxygen
Colors
Designer to choose colors to be used in the design.
Look and feel

```html
<!DOCTYPE html>
<html lang="en">
<head>
<meta charset="utf-8">
<title>FloorBright Digital – Marketing Capabilities Overview</title>
<link href="https://fonts.googleapis.com/css2?family=Bebas+Neue&family=Montserrat:ital,wght@0,400;0,600;0,700;0,800;1,600;1,700&display=swap" rel="stylesheet">
<style>
:root{
  --canvas:#d8d9db;
  --blue:#5a67c6;
  --lite-blue:#3aa7e2;
  --charcoal:#38393e;
  --charcoal-2:#2c2d31;
  --black:#0e0e10;
  --white:#ffffff;
  --paper:#f4f4f5;
  --grey:#9b9ca3;
  --red:#d6322b;
  --text:#3b3c42;
  --gold:#f2b33a;
}
*{box-sizing:border-box;margin:0;padding:0}
html,body{width:1176px;height:1200px;overflow:hidden;background:var(--canvas)}
body{position:relative;font-family:'Montserrat',sans-serif;color:var(--text)}
.guide{position:absolute;top:41px;width:1px;height:1122px;background:#e06a63;z-index:5}
.spread{position:absolute;width:495px;height:320px;overflow:hidden;background:var(--white);box-shadow:0 1px 3px rgba(0,0,0,.12)}
.abs{position:absolute}
.head{font-family:'Bebas Neue',sans-serif;letter-spacing:.2px;line-height:1}
.band{position:absolute;background:var(--blue);color:var(--white);font-family:'Bebas Neue',sans-serif;font-size:10.5px;padding-left:22px;display:flex;align-items:center}
.focus{position:absolute;background:var(--lite-blue);color:var(--white);font-size:4px;font-weight:700;text-align:center;display:flex;align-items:center;justify-content:center}
.body{position:absolute;font-size:3.6px;line-height:1.38;text-align:justify}
.kick{position:absolute;font-size:3.9px;font-weight:700;color:var(--lite-blue);line-height:1.25}
.bul{position:absolute;font-size:3.6px;line-height:1.38;padding-left:6px}
.bul p{position:relative;margin-bottom:2px}
.bul p::before{content:"";position:absolute;left:-5px;top:1.5px;width:2px;height:2px;border-radius:50%;background:var(--lite-blue)}
.bul b{font-weight:700;font-style:italic}
.on-dark{color:#d9dae0}
.ph{position:absolute;border-radius:2px}
.foot{position:absolute;left:0;bottom:0;width:495px;height:8px;font-size:3.4px;color:var(--white)}
.foot .tag{position:absolute;top:0;height:8px;width:30px;background:var(--black);display:flex;align-items:center;padding-left:5px}
.foot .tag.r{right:0;justify-content:flex-end;padding-right:5px}
.foot .bar{position:absolute;top:2.5px;height:5.5px;display:flex;align-items:center}
.foot .bar.l{left:30px;width:218px;justify-content:flex-end;padding-right:10px}
.foot .bar.r{left:248px;width:217px;padding-left:10px}
.dark{background:var(--charcoal)}
.grid-table{position:absolute;background:var(--white);border:0.6px solid #555}
.grid-table div{display:flex;border-bottom:0.4px solid #d5d5d8;height:6.7px;align-items:center;font-size:2.2px;color:#444}
.grid-table div span{flex:1;padding-left:2px}
.grid-table div span:first-child{flex:2.2}
.grid-table .th{background:#eef0f6;font-weight:700}
.pill{position:absolute;height:11px;width:52px;border-radius:6px;background:var(--blue);color:var(--white);font-size:2.6px;font-weight:700;display:flex;align-items:center;justify-content:center;text-align:center;line-height:1.1}
.pill.w{background:var(--white);color:var(--blue)}
.bubble{position:absolute;font-size:2.4px;line-height:1.25;padding:1.5px 2px;border-radius:3px}
.bubble.me{background:#3a86f0;color:#fff}
.bubble.them{background:#e9e9eb;color:#222}
.icon-row{position:absolute;left:382px;display:flex;align-items:center;gap:6px}
.icon-row .ico{width:19px;height:19px;background:var(--white);border-radius:2px;display:flex;align-items:center;justify-content:center}
.icon-row .t{font-size:3.6px;color:var(--white);line-height:1.25}
.icon-row .t b{font-weight:700;display:block}
.stat{position:absolute;text-align:center;width:70px}
.stat .n{font-weight:800;font-size:14px;color:var(--blue);line-height:1}
.stat .l{font-size:3.8px;margin-top:5px;color:#333}
</style>
</head>
<body>

<div class="guide" style="left:321px"></div>
<div class="guide" style="left:854px"></div>

<!-- ===== Spread: cover ===== -->
<section class="spread" style="left:74px;top:91px;background:#f6f6f7">
  <div class="abs" style="left:17px;top:94px;width:114px;height:28px;border:1.2px solid var(--black);background:var(--white);display:flex;flex-direction:column;align-items:center;justify-content:center">
    <span style="font-weight:800;font-size:11px;color:var(--black);letter-spacing:-.4px;line-height:1">FLOORBRIGHT</span>
    <span style="font-weight:600;font-size:4.5px;color:var(--black);letter-spacing:1.4px;align-self:flex-end;margin-right:8px">DIGITAL</span>
  </div>
  <div class="band" style="left:0;top:196px;width:152px;height:31px;font-size:20px;padding-left:15px">LET'S GET STARTED</div>
  <p class="abs" style="left:15px;top:235px;width:130px;font-size:3.6px;line-height:1.4;color:#333">Grow your concrete coating business with proven marketing systems designed to drive real results.</p>
  <div class="abs head" style="left:15px;top:261px;font-size:9px;color:var(--blue)">CONTACT US:</div>
  <ul class="abs" style="left:15px;top:275px;list-style:none;font-size:3.6px;line-height:2.2;color:#333">
    <li>FloorBright Digital</li>
    <li>&#9742;&nbsp; 555-318-2047</li>
    <li>&#9993;&nbsp; info@floorbrightdigital.com</li>
    <li>&#9675;&nbsp; FloorBrightDigital.com</li>
  </ul>
  <div class="ph" role="img" aria-label="Photo of a finished garage with flake epoxy floor, grey cabinets and a wall-mounted bike" style="left:152px;top:0;width:343px;height:320px;border-radius:0;background:linear-gradient(180deg,#4a5468 0%,#7c8494 38%,#a4a8b0 60%,#8e9199 100%)"></div>
  <div class="abs" style="left:375px;top:14px;width:120px;height:28px;background:var(--black);display:flex;flex-direction:column;align-items:center;justify-content:center">
    <span style="font-weight:800;font-size:9px;color:var(--white);letter-spacing:-.3px;line-height:1">FLOORBRIGHT</span>
    <span style="font-size:3.6px;color:var(--white);letter-spacing:1.2px">DIGITAL</span>
  </div>
  <div class="abs" style="left:375px;top:58px;width:100px;height:205px;background:var(--blue);padding:24px 8px 0 8px">
    <div class="head" style="font-size:20.5px;color:var(--white);line-height:1.28">MARKETING<br>CAPABILITIES<br>OVERVIEW</div>
    <p style="position:absolute;left:8px;top:180px;font-size:2.8px;line-height:1.35;color:#e8eaf8;width:84px">Helping Concrete Coating Companies Generate Leads, Close Sales, and Grow with Proven Digital Strategies</p>
  </div>
  <div class="abs" style="left:375px;top:302px;width:120px;height:9px;background:var(--black);color:var(--white);font-size:3.4px;display:flex;align-items:center;justify-content:flex-end;padding-right:8px">www.floorbrightdigital.com</div>
</section>

<!-- ===== Spread: pages 1–2 ===== -->
<section class="spread" style="left:607px;top:91px">
  <div class="abs" style="left:14px;top:0;width:86px;height:82px;background:var(--black)"></div>
  <div class="ph" role="img" aria-label="Exploded view of floor coating layers: flake top coat, black base and tan primer over a concrete slab" style="left:35px;top:17px;width:205px;height:182px;background:linear-gradient(160deg,#e9e9ea 0%,#9a9a9c 35%,#2b2b2d 50%,#c9b79b 62%,#9b9b9d 80%,#7d7d80 100%)"></div>
  <div class="abs head" style="left:14px;top:211px;font-size:12.5px;color:var(--blue)">WHO WE ARE</div>
  <p class="body" style="left:14px;top:228px;width:226px">At FloorBright Digital, we specialize in helping concrete coating companies grow through practical, results-driven marketing. Whether you're looking to generate high-quality leads, tighten up your sales process, or build a steady pipeline of future jobs, our strategies are built to get real, measurable results. With years of marketing experience in the home services space, we know the challenges you face—and we've developed a suite of marketing solutions designed to deliver measurable results.</p>
  <div class="stat" style="left:14px;top:273px"><div class="n">$5M+</div><div class="l">CLIENT REVENUE</div></div>
  <div class="stat" style="left:89px;top:273px"><div class="n">$1M+</div><div class="l">ADS MANAGED</div></div>
  <div class="stat" style="left:160px;top:273px"><div class="n">3000+</div><div class="l">LEADS GENERATED</div></div>

  <div class="abs" style="left:251px;top:5px;font-size:4.2px;font-weight:600;color:#222">&#9679; Friendbook Feed</div>
  <div class="abs" style="left:373px;top:5px;font-size:4.2px;font-weight:600;color:#222">&#9633; Snapgram feed</div>
  <div class="abs" style="left:251px;top:14px;width:113px;height:204px;background:#f7f7f8;border:0.5px solid #ddd">
    <div style="font-size:2.8px;padding:4px 3px;color:#222;line-height:1.5"><b>Slabcraft Coatings</b><br>Chicagoland Homeowners!<br>Tired of ugly old cracked and ... See more</div>
    <div class="ph" role="img" aria-label="Video ad still of a grey flake floor with the headline Attention Chicago area homeowners" style="left:8px;top:30px;width:97px;height:125px;background:linear-gradient(180deg,#e4e2dd 0%,#8f8f8f 55%,#6d6d6f 100%)"></div>
    <div style="position:absolute;left:8px;top:165px;font-size:2.8px;line-height:1.4;color:#222">FORM ON FRIENDBOOK<br><b>Professional Concrete<br>Coatings</b></div>
    <div style="position:absolute;left:80px;top:168px;font-size:2.8px;background:#e4e6eb;padding:2px 3px;border-radius:1px;font-weight:700">Get quote</div>
  </div>
  <div class="abs" style="left:373px;top:14px;width:114px;height:204px;background:#f7f7f8;border:0.5px solid #ddd">
    <div style="font-size:2.8px;padding:4px 3px;color:#222;line-height:1.5;text-align:center"><b>Snapgram</b></div>
    <div style="font-size:2.8px;padding:0 3px;color:#222"><b>Slabcraft Coatings</b> · Sponsored</div>
    <div class="ph" role="img" aria-label="Ad photo of a speckled coated floor with the headline Professional Concrete Coating" style="left:0;top:28px;width:114px;height:112px;border-radius:0;background:linear-gradient(180deg,#7b7b7d 0%,#a9a9ab 50%,#6e6e72 100%)"></div>
    <div style="position:absolute;left:0;top:128px;width:114px;height:7px;background:var(--blue);font-size:2.4px;color:#fff;display:flex;align-items:center;justify-content:center">SLABCRAFTCOATINGS.COM | (555) 014-2290</div>
    <div style="position:absolute;left:3px;top:145px;font-size:2.8px;color:#222">Get quote</div>
    <div style="position:absolute;left:3px;top:170px;font-size:2.8px;color:#222">Chicagoland Homeowners!</div>
  </div>
  <div class="abs" style="left:248px;top:220px;width:247px;height:92px;background:var(--blue)">
    <div class="head" style="position:absolute;left:14px;top:17px;font-size:13px;color:var(--lite-blue)">WHAT WE DO</div>
    <div style="position:absolute;left:14px;top:34px;font-size:6px;font-weight:700;font-style:italic;color:var(--white)">FloorBright Digital Marketing Solutions</div>
    <div style="position:absolute;left:14px;top:42px;font-size:3.6px;color:#e4e6f6">Proven Strategies to Drive Consistent, High-Quality Leads for Your Business</div>
    <p class="body" style="left:14px;top:52px;width:222px;color:#e4e6f6;text-align:left">At FloorBright Digital, we've developed a powerful, no-nonsense system designed to help concrete coating businesses attract and convert more leads. Our two-tiered approach offers flexibility based on your needs — whether you're just looking for leads or want a full marketing system to maximize your results.</p>
  </div>
  <div class="foot">
    <span class="tag">PAGE 1</span>
    <span class="bar l" style="background:var(--lite-blue)">www.floorbrightdigital.com</span>
    <span class="bar r" style="background:var(--blue)">www.floorbrightdigital.com</span>
    <span class="tag r">PAGE 2</span>
  </div>
</section>

<!-- ===== Spread: pages 3–4 ===== -->
<section class="spread" style="left:74px;top:440px">
  <div class="abs dark" style="left:0;top:0;width:495px;height:179px;background:linear-gradient(135deg,#3d3e43,#2e2f33)"></div>
  <div class="abs" style="left:0;top:179px;width:495px;height:3px;background:var(--lite-blue)"></div>
  <div class="abs" style="left:0;top:182px;width:495px;height:130px;background:linear-gradient(180deg,#ffffff,#f1f1f2)"></div>
  <div class="band" style="left:0;top:17px;width:233px;height:19px">OPTION 1: LEAD GENERATION ADS SYSTEM</div>
  <p class="body on-dark" style="left:14px;top:45px;width:219px;text-align:left">Get Qualified Leads Flowing into Your Business</p>
  <p class="body on-dark" style="left:14px;top:56px;width:219px">Friendbook &amp; Snapgram Lead Generation<br>Turn Social Media Into a Lead Machine<br>We help you connect with potential customers where they're already spending their time. Our targeted Friendbook and Snapgram ad campaigns are designed specifically for concrete coating businesses.</p>
  <div class="focus" style="left:14px;top:90px;width:219px;height:10px">WE FOCUS ON:</div>
  <div class="grid-table" style="left:14px;top:109px;width:122px;height:81px">
    <div class="th"><span>Campaign name</span><span>Reach</span><span>Impressions</span><span>Results</span></div>
    <div><span>Partners Program - Application</span><span>104,232</span><span>461,152</span><span>21</span></div>
    <div><span>Product Feature Campaign</span><span>4,265</span><span>21,264</span><span>18</span></div>
    <div><span>Conversions - Products</span><span>63,660</span><span>194,693</span><span>96</span></div>
    <div><span>Conversions - Spring Line</span><span>21,037</span><span>108,820</span><span>35</span></div>
    <div><span>Conversions - Holiday Offer</span><span>11,672</span><span>82,946</span><span>12</span></div>
    <div><span>Conversions - Webinar Series</span><span>143,804</span><span>613,738</span><span>33</span></div>
    <div><span>Conversions - Spring Training</span><span>32,346</span><span>159,067</span><span>34</span></div>
    <div><span>Conversions - August Webinar</span><span>22,616</span><span>77,861</span><span>0</span></div>
  </div>
  <div class="kick" style="left:144px;top:110px;width:90px">Highly Targeted Audience Selection</div>
  <p class="body on-dark" style="left:144px;top:122px;width:89px">We use advanced targeting strategies to ensure your ads are seen by homeowners most likely to want concrete coating services. This means better leads and less wasted ad spend.</p>
  <div class="bul on-dark" style="left:144px;top:155px;width:89px"><p>Hyper-Targeted Ad Campaigns: We reach the right audience in your service area.</p></div>

  <div class="kick" style="left:261px;top:19px;font-size:3.9px">Strong Offers That Drive Action</div>
  <p class="body on-dark" style="left:261px;top:26px;width:118px">A good offer can make or break your ad campaign. We help you craft irresistible offers that encourage leads to take the next step, whether it's a free estimate, a limited-time discount, or a special promotion.</p>
  <div class="abs" style="left:388px;top:17px;width:91px;height:154px;background:var(--white);border-radius:2px">
    <div class="bubble me" style="left:24px;top:15px;width:63px">Do you have a rough idea how many leads converted and then the referrals that came from those leads?</div>
    <div class="bubble them" style="left:4px;top:37px;width:60px">So far 3 leads have converted.</div>
    <div class="bubble them" style="left:4px;top:45px;width:60px">And I got 1 referral that converted from that.</div>
    <div class="bubble them" style="left:4px;top:56px;width:60px">So 4 total conversions stemming from Friendbook ads.</div>
    <div class="bubble me" style="left:27px;top:70px;width:60px">Got it. What was the total revenue for those?</div>
    <div class="bubble them" style="left:4px;top:85px;width:30px">$11,400</div>
    <div class="bubble them" style="left:4px;top:92px;width:45px">One of them is a $6K job</div>
    <div class="bubble me" style="left:27px;top:105px;width:60px">Nice! How many of the other leads' quotes are still pending or look solid? Trying to get an idea of the overall picture of where things are</div>
  </div>

  <div class="kick" style="left:14px;top:209px;width:90px">Attention-Grabbing Creative (Images, Videos, and Copy)</div>
  <p class="body" style="left:14px;top:222px;width:110px">We craft high-quality visuals and compelling ad copy designed to stop people in their tracks and make them take action. A strong first impression means higher engagement and better results.</p>
  <div class="bul" style="left:14px;top:253px;width:110px"><p>Scroll-Stopping Creative: Engaging images, videos, and offers tailored to convert.</p></div>
  <div class="ph" role="img" aria-label="Two social feed ad mockups showing coated garage floor ads" style="left:140px;top:207px;width:93px;height:88px;background:linear-gradient(180deg,#f4f4f5,#9fa0a4 55%,#e9e9ea);border:0.5px solid #bbb"></div>

  <div class="abs" style="left:261px;top:193px;width:125px;height:98px;background:var(--white);border:0.6px solid #444">
    <div style="position:absolute;left:4px;top:3px;font-weight:800;font-size:5px;line-height:1.05"><span style="color:var(--red)">46 NEW CUSTOMERS</span><br><span style="color:var(--black)">IN JUST TWO MONTHS</span></div>
    <div class="ph" role="img" aria-label="Holiday lighting ad results screenshot with ad preview" style="left:4px;top:18px;width:82px;height:76px;background:linear-gradient(180deg,#e9ecf2,#c6cad3);border-radius:0"></div>
    <div class="ph" role="img" aria-label="Holiday lighting installation ad photo" style="left:82px;top:0;width:43px;height:28px;border-radius:0;background:linear-gradient(135deg,#1e2a1f,#5b4b23)"></div>
    <div style="position:absolute;left:86px;top:67px;font-weight:800;font-style:italic;font-size:6px;line-height:1.05;text-align:center"><span style="color:var(--red)">475 LEADS</span><br><span style="color:var(--black);font-size:5px">IN FIVE<br>MONTHS</span></div>
  </div>
  <div class="kick" style="left:394px;top:193px;width:90px">Lead Forms Designed to Capture Customer Information Directly From the Platform</div>
  <p class="body" style="left:394px;top:211px;width:90px">Our seamless lead forms make it easy for potential customers to submit their information without ever leaving Friendbook or Snapgram. This reduces friction, increases conversions, and gets you more leads with less hassle.</p>
  <div class="bul" style="left:394px;top:253px;width:90px"><p>Seamless Lead Capture: In-platform lead forms that deliver leads straight to your phone and inbox.</p></div>

  <div class="foot">
    <span class="tag">PAGE 3</span>
    <span class="bar l" style="background:var(--blue)">www.floorbrightdigital.com</span>
    <span class="bar r" style="background:var(--blue)">www.floorbrightdigital.com</span>
    <span class="tag r">PAGE 4</span>
  </div>
</section>

<!-- ===== Spread: pages 5–6 ===== -->
<section class="spread" style="left:607px;top:440px">
  <div class="abs" style="left:0;top:179px;width:495px;height:3px;background:var(--lite-blue)"></div>
  <div class="abs dark" style="left:0;top:182px;width:495px;height:130px;background:linear-gradient(135deg,#3d3e43,#2e2f33)"></div>
  <div class="ph" role="img" aria-label="Two phones showing lead alert text messages and a floor coating lead ad" style="left:15px;top:20px;width:130px;height:158px;background:linear-gradient(180deg,#f2ede4,#d8d2c6);border-radius:8px"></div>
  <div class="kick" style="left:157px;top:22px">Leads delivered directly to you</div>
  <p class="body" style="left:157px;top:30px;width:82px">We then immediately deliver leads straight to your phone and email for quick follow-up – or can integrate and push leads to your CRM if you already have one.</p>

  <div class="band" style="left:262px;top:17px;width:233px;height:19px;padding-left:10px">OPTION 2: FULL MARKETING SYSTEM</div>
  <p class="body" style="left:262px;top:47px;width:222px;text-align:left">Everything in Our Lead Generation System — Plus Powerful Tools to Help You Close More Sales and Build Long-Term Trust</p>
  <div class="focus" style="left:262px;top:63px;width:219px;height:9px">OUR FULL MARKETING SYSTEM INCLUDES:</div>
  <div class="ph" role="img" aria-label="Laptop and phone displaying the CRM pipeline dashboard" style="left:269px;top:85px;width:126px;height:87px;background:linear-gradient(180deg,#eef0f5,#c9ccd5);border-radius:3px"></div>
  <div class="kick" style="left:405px;top:88px">CRM Setup &amp; Integration</div>
  <p class="body" style="left:405px;top:95px;width:80px">We help you streamline your lead management and sales process. We'll help you organize your leads and sales process so you can focus on closing deals.</p>
  <div class="bul" style="left:405px;top:125px;width:80px"><p><b>Custom CRM Solutions:</b> Set up or integrate a CRM tailored to your business.</p><p><b>Optimized Sales Pipeline:</b> Streamline lead tracking and management</p></div>

  <div class="kick" style="left:14px;top:197px">Retargeting Ads - Stay Top of Mind</div>
  <p class="body on-dark" style="left:14px;top:206px;width:90px">Leads need reminders. Our retargeting campaigns keep your business top of mind for people who've already shown interest.</p>
  <p class="body on-dark" style="left:14px;top:230px;width:90px">With this system, you'll start seeing a steady flow of high-quality leads, giving your business a predictable and scalable way to grow</p>
  <svg class="abs" style="left:110px;top:195px" width="125" height="105" viewBox="0 0 125 105" aria-hidden="true">
    <g stroke="#c9cbe6" stroke-width=".5" fill="none">
      <path d="M58 7 H65"/><path d="M91 12 Q100 20 88 25 H60"/><path d="M31 18 V23"/>
      <path d="M58 28 H65"/><path d="M91 33 Q100 40 88 46 H60"/><path d="M60 51 H65"/>
      <path d="M91 54 Q95 62 78 66"/><path d="M53 77 V83"/>
    </g>
  </svg>
  <div class="pill" style="left:113px;top:197px">New lead Sent Through Flowlink</div>
  <div class="pill" style="left:176px;top:197px">Follow Up Text Drip 1 Sent</div>
  <div class="pill" style="left:113px;top:218px">Follow Up Email Drip 2 Sent</div>
  <div class="pill w" style="left:176px;top:218px">Wait 1 Day</div>
  <div class="pill w" style="left:116px;top:239px">Wait 1 Day</div>
  <div class="pill" style="left:176px;top:239px">Follow Up Email Drip 3 Sent</div>
  <div class="pill" style="left:145px;top:262px">Client Opened Follow Up 3</div>
  <div class="pill" style="left:145px;top:283px">Client Booked Appointment</div>

  <svg class="abs" style="left:257px;top:188px" width="141" height="92" viewBox="0 0 141 92" aria-label="Follow-up cycle chart: email, text, seasonal promotions, special offers and limited-time deals" role="img">
    <g transform="translate(70 46)" fill="none" stroke-width="15">
      <circle r="31" stroke="#7aa5dd"/>
      <path d="M-31 0 A31 31 0 0 1 0 -31" stroke="var(--gold)"/>
      <path d="M0 -31 A31 31 0 0 1 31 0" stroke="var(--gold)"/>
      <path d="M-22 22 A31 31 0 0 1 -31 0" stroke="var(--blue)"/>
      <path d="M22 22 A31 31 0 0 1 -22 22" stroke="var(--blue)"/>
    </g>
    <circle cx="70" cy="46" r="21" fill="#ffffff"/>
    <g font-family="Montserrat,sans-serif" font-size="3" fill="#ffffff" text-anchor="middle">
      <text x="12" y="7">Email</text><text x="12" y="11">Follow-up</text>
      <text x="128" y="14">Limited-Time</text><text x="128" y="18">Deals</text>
      <text x="130" y="52">Text</text><text x="130" y="56">Follow-up</text>
      <text x="12" y="62">Special</text><text x="12" y="66">Offers</text>
      <text x="118" y="86">Seasonal</text><text x="118" y="90">Promotions</text>
    </g>
  </svg>
  <div class="kick" style="left:405px;top:197px;width:85px">Automated Lead Follow-Up – Never Let a Lead Slip Through the Cracks</div>
  <div class="bul on-dark" style="left:405px;top:214px;width:85px"><p><b>Instant Text &amp; Email Responses:</b> Engage leads right when they come in.</p><p><b>Automated follow-up for each stage of your sales pipeline:</b> New lead follow-up, Project estimate follow-up, Installation day reminders - all to help keep leads moving forward.</p></div>
  <p class="body on-dark" style="left:261px;top:281px;width:225px">Quick follow-ups are critical to converting leads into clients. Our system does it for you. We send instant text and email alerts to your sales team while also automating follow-up with your leads. This ensures no lead goes cold.</p>

  <div class="foot">
    <span class="tag">PAGE 5</span>
    <span class="bar l" style="background:var(--blue)">www.floorbrightdigital.com</span>
    <span class="bar r" style="background:var(--blue)">www.floorbrightdigital.com</span>
    <span class="tag r">PAGE 6</span>
  </div>
</section>

<!-- ===== Spread: pages 7–8 ===== -->
<section class="spread" style="left:74px;top:787px">
  <div class="abs dark" style="left:0;top:0;width:495px;height:158px;background:linear-gradient(135deg,#3d3e43,#2e2f33)"></div>
  <div class="abs" style="left:0;top:158px;width:495px;height:3px;background:var(--lite-blue)"></div>
  <div class="abs" style="left:0;top:161px;width:495px;height:151px;background:linear-gradient(180deg,#ffffff,#f1f1f2)"></div>
  <div class="ph" role="img" aria-label="Phone showing a stack of appointment-booked notifications" style="left:19px;top:16px;width:92px;height:124px;background:linear-gradient(160deg,#4b5a86,#2c3a60 60%,#5d6fa8);border-radius:8px"></div>
  <div class="kick" style="left:141px;top:17px;width:100px">Long-Term Lead Nurture Campaigns – Turn Cold Leads Into Future Customers</div>
  <p class="body on-dark" style="left:141px;top:31px;width:92px">Stay top of mind with leads not ready to commit yet and win them over in the long run. Our long-term email and text nurture sequences are designed to keep your business top of mind, build trust over time, and showcase your expertise.</p>
  <div class="bul on-dark" style="left:141px;top:67px;width:92px"><p><b>Strategic Email &amp; Text Sequences:</b> Automated messages that consistently build <b>Trust and keep the conversation going.</b></p><p><b>Re-Engagement Campaigns:</b> Use exclusive offers and timely updates to bring old leads back into the mix</p></div>

  <div class="kick" style="left:262px;top:24px">Lead Tracking System</div>
  <p class="body on-dark" style="left:262px;top:32px;width:70px;text-align:left">We provide a customized lead tracking and management system so you can see exactly where leads are in the sales process — no guessing, no confusion.</p>
  <div class="grid-table" style="left:338px;top:33px;width:142px;height:97px">
    <div class="th" style="height:13px"><span>Results</span><span>Cost per result</span><span>Amount spent</span><span>Purchases conversion value</span></div>
    <div style="height:10.5px"><span>263 Partner Application</span><span>$28.16</span><span>$5,301.92</span><span>$134,828.66</span></div>
    <div style="height:10.5px"><span>82 Website purchases</span><span>$3.08</span><span>$252.61</span><span>$63,047.09</span></div>
    <div style="height:10.5px"><span>88 Website purchases</span><span>$54.53</span><span>$2,399.43</span><span>$20,891.31</span></div>
    <div style="height:10.5px"><span>30 Website purchases</span><span>$180.10</span><span>$1,801.04</span><span>$7,216.14</span></div>
    <div style="height:10.5px"><span>3 Website purchases</span><span>$131.83</span><span>$394.45</span><span>$7,105.00</span></div>
    <div style="height:10.5px"><span>835 Website Completed</span><span>$8.73</span><span>$7,285.70</span><span>$6,797.70</span></div>
    <div style="height:10.5px"><span>4 Website purchases</span><span>$560.05</span><span>$2,240.22</span><span>$3,851.78</span></div>
    <div style="height:10.5px;border:0"><span>118 Website Completed</span><span>$13.74</span><span>$1,620.76</span><span>$3,140.70</span></div>
  </div>

  <div class="kick" style="left:14px;top:180px;width:90px">Customer Follow-Up for Reviews &amp; Testimonials – Build Trust With Every Project</div>
  <p class="body" style="left:14px;top:199px;width:92px">Your online reputation is a powerful tool for attracting new business. Once a job is completed, we reach out to satisfied customers, helping you build a strong reputation with positive Reviewly reviews and testimonials.</p>
  <div class="bul" style="left:14px;top:236px;width:92px"><p><b>Automated Review Requests:</b> Make it easy for satisfied customers to leave feedback.</p><p><b>Boosted Visibility:</b> Improve your ranking on Reviewly to attract more business</p></div>
  <div class="abs" style="left:134px;top:180px;width:85px;text-align:center">
    <div style="font-weight:700;font-size:17px;color:#4a4b52;line-height:1">Reviewly</div>
    <div style="font-size:4.2px;color:#333;margin-top:2px">Reviews</div>
    <div style="font-size:4.2px;color:#333">5.0 <span style="color:var(--gold)">★★★★★</span></div>
  </div>
  <div class="abs" style="left:121px;top:230px;width:95px;height:55px;background:linear-gradient(135deg,#fbe9ef,#efe4f6)">
    <div style="position:absolute;left:14px;top:14px;width:68px;height:27px;background:var(--white);border-radius:3px;box-shadow:0 1px 3px rgba(0,0,0,.15);text-align:center;padding-top:3px">
      <div style="color:var(--gold);font-size:10px;line-height:1">★★★★★</div>
      <div style="font-size:5px;font-weight:600;color:#333;margin-top:2px"><span style="display:inline-block;width:4px;height:4px;border-radius:50%;background:#7d7e86;margin-right:2px"></span>5.0 average rating</div>
    </div>
  </div>
  <div class="ph" role="img" aria-label="Laptop and phone showing a floor coating company website" style="left:262px;top:177px;width:124px;height:85px;background:linear-gradient(180deg,#2b2c31 0%,#b98e69 45%,#d9d5cf 100%);border-radius:3px"></div>
  <div class="kick" style="left:400px;top:180px">Regular Reporting &amp; Strategy Calls</div>
  <p class="body" style="left:400px;top:188px;width:85px;text-align:left">We review campaign performance, identify trends, and make adjustments to improve results month after month.</p>
  <p class="body" style="left:400px;top:210px;width:85px;text-align:left">This system is ideal for businesses that want a complete solution to generate leads, follow up efficiently, and maximize every opportunity.</p>

  <div class="foot">
    <span class="tag">PAGE 7</span>
    <span class="bar l" style="background:var(--blue)">www.floorbrightdigital.com</span>
    <span class="bar r" style="background:var(--blue)">www.floorbrightdigital.com</span>
    <span class="tag r">PAGE 8</span>
  </div>
</section>

<!-- ===== Spread: pages 9–10 ===== -->
<section class="spread" style="left:607px;top:787px">
  <div class="band" style="left:0;top:17px;width:233px;height:21px">OPTION 1: LEAD GENERATION ADS SYSTEM</div>
  <div class="bul" style="left:14px;top:48px;width:89px"><p>If you're just looking to <b>get more leads</b>, our <b>Lead Generation Ads System</b> is a solid starting point.</p><p>If you're serious about maximizing your results, nurturing leads, and building a strong reputation, our <b>Full Marketing System</b> is the best way to ensure no opportunity is missed.</p></div>
  <div class="abs" style="left:113px;top:51px;font-weight:700;font-size:9px;line-height:1.1;color:var(--black)">33 New Coating Leads<br><span style="color:var(--red)">in <u>1 Month</u>...</span></div>
  <div class="ph" role="img" aria-label="Collage of lead ad screenshots and a results table" style="left:106px;top:78px;width:136px;height:71px;background:linear-gradient(135deg,#eceef3,#b9bdc7 50%,#e6e7eb);border:0.5px solid #c6c6c9"></div>
  <div class="band" style="left:0;top:161px;width:233px;height:20px">OPTION 1: LEAD GENERATION ADS SYSTEM</div>
  <p class="body" style="left:14px;top:192px;width:110px;text-align:left">We don't just run ads—we build effective systems that actually grow your business.</p>
  <div class="bul" style="left:14px;top:209px;width:92px"><p><b>Industry Expertise:</b> We focus exclusively on working with concrete coating companies.</p><p><b>Proven ROI:</b> Every strategy we implement is focused on what actually moves the needle. No fluff. Just Results.</p><p><b>Full-Service Solutions:</b> From lead generation to streamlined sales systems, we build complete marketing setups for concrete coating companies at any stage of growth.</p></div>
  <div class="ph" role="img" aria-label="Exploded view of flake coating layers over a concrete slab" style="left:140px;top:195px;width:106px;height:111px;background:linear-gradient(170deg,#dcdcdc 0%,#8fb4dc 40%,#e8eef6 60%,#bdbdbf 100%)"></div>

  <div class="ph" role="img" aria-label="CRM opportunities board with lead pipeline columns" style="left:249px;top:0;width:246px;height:168px;border-radius:0;background:linear-gradient(90deg,#2d3b4f 0 12%,#f4f5f8 12% 100%)"></div>
  <div class="abs" style="left:248px;top:168px;width:247px;height:144px;background:var(--blue)">
    <div class="head" style="position:absolute;left:14px;top:9px;font-size:12px;color:var(--lite-blue)">TEST DRIVE OUR ADS SYSTEM!</div>
    <div style="position:absolute;left:14px;top:29px;width:110px;font-size:3.8px;font-weight:700;font-style:italic;color:var(--white);line-height:1.35">Get 30 Days of Concrete Coating Leads for $97 (+ Ad Spend)</div>
    <p style="position:absolute;left:14px;top:45px;width:110px;font-size:3.6px;color:#e4e6f6;line-height:1.38">We'll set up and manage your Friendbook and Snapgram ads, send exclusive leads directly to you, and even integrate with your CRM if needed.</p>
    <div style="position:absolute;left:14px;top:96px;font-size:2.8px;color:#e4e6f6">Test-drive our ads system for 30 days for just $97 (+ Ad Spend)</div>
    <div class="head" style="position:absolute;left:14px;top:105px;font-size:9px;color:var(--white)">TEXT OR CALL NOW TO GET STARTED!</div>
    <div class="head" style="position:absolute;left:14px;top:114px;width:104px;height:15px;border-radius:8px;background:var(--lite-blue);color:var(--white);font-size:12px;display:flex;align-items:center;justify-content:center">555-318-2047</div>
  </div>
  <div class="icon-row" style="top:179px"><span class="ico"><svg width="11" height="11" viewBox="0 0 12 12"><path d="M2 1h6l2 2v8H2z M4 5h4 M4 7h4" fill="none" stroke="#5a67c6" stroke-width=".9"/></svg></span><span class="t"><b>No Contracts.</b><b>No Fluff. Just Leads.</b></span></div>
  <div class="icon-row" style="top:204px"><span class="ico"><svg width="11" height="11" viewBox="0 0 12 12"><circle cx="6" cy="6" r="4.5" fill="none" stroke="#5a67c6" stroke-width=".9"/><path d="M4 6l1.5 1.5L8.5 4.5" fill="none" stroke="#5a67c6" stroke-width=".9"/></svg></span><span class="t"><b>Exclusive Leads</b>No sharing or competing</span></div>
  <div class="icon-row" style="top:229px"><span class="ico"><svg width="11" height="11" viewBox="0 0 12 12"><rect x="2" y="2" width="8" height="8" rx="1" fill="none" stroke="#5a67c6" stroke-width=".9"/><path d="M4 5h4M4 7h3" stroke="#5a67c6" stroke-width=".9"/></svg></span><span class="t"><b>CRM Integration</b>Works with your system</span></div>
  <div class="icon-row" style="top:254px"><span class="ico"><svg width="11" height="11" viewBox="0 0 12 12"><rect x="3.5" y="1.5" width="5" height="9" rx="1" fill="none" stroke="#5a67c6" stroke-width=".9"/><circle cx="6" cy="9" r=".5" fill="#5a67c6"/></svg></span><span class="t"><b>Leads Sent Instantly</b>Directly to your phone &amp; email</span></div>
  <div class="icon-row" style="top:279px"><span class="ico"><svg width="11" height="11" viewBox="0 0 12 12"><circle cx="6" cy="6" r="2" fill="none" stroke="#5a67c6" stroke-width=".9"/><path d="M6 1v2M6 9v2M1 6h2M9 6h2" stroke="#5a67c6" stroke-width=".9"/></svg></span><span class="t"><b>Full Ad Setup &amp; Management</b>Friendbook &amp; Snapgram</span></div>

  <div class="foot">
    <span class="tag">PAGE 9</span>
    <span class="bar l" style="background:var(--lite-blue)">www.floorbrightdigital.com</span>
    <span class="bar r" style="background:var(--blue)">www.floorbrightdigital.com</span>
    <span class="tag r">PAGE 10</span>
  </div>
</section>

</body>
</html>
```